Skyreach Northern Flights
Private Charters
Skyreach Northern Flights  - Aviation
Creative Brief
Cutting-Edge
Tamara Holbrook
Business Development
5127 N. Darrow, Suite 240 Scottsdale, AZ 85254
tholbrook@skyreachnorthernflights.example
www.skyreachnorthernflights.example

```html
<!DOCTYPE html>
<html lang="en">
<head>
<meta charset="utf-8">
<title>Skyreach Northern Flights – Stationery</title>
<link rel="stylesheet" href="https://fonts.googleapis.com/css2?family=Cinzel:wght@400;600&family=Lato:wght@400;700&display=swap">
<style>
  :root{
    --backdrop:#a9abae;
    --paper:#ffffff;
    --maroon:#6a2823;
    --accent-red:#8e2c25;
    --charcoal:#5c5755;
    --ink:#4a4644;
    --muted:#8d8987;
    --card-tint:#e9dcda;
  }
  *{margin:0;padding:0;box-sizing:border-box}
  html,body{width:1200px;height:667px;overflow:hidden;background:var(--backdrop)}
  .canvas{position:relative;width:1200px;height:667px;background:var(--backdrop);font-family:"Lato",sans-serif;color:var(--ink)}
  .sheet{position:absolute;background:var(--paper);box-shadow:0 1px 3px rgba(0,0,0,.25)}
  .wordmark{text-align:center;font-family:"Cinzel",serif;font-weight:400;color:var(--charcoal);line-height:1.1;white-space:nowrap}
  .wordmark .mark-dot{display:block;width:10px;height:10px;margin:0 auto 5px;background:var(--accent-red);border-radius:50%}
  .wordmark .name{display:block;letter-spacing:.5px}
  .wordmark .tag{display:block;font-size:.55em;letter-spacing:3px;margin-top:2px}
  .wordmark.light{color:#fff}
  .wordmark.light .mark-dot{background:#fff}

  /* letterhead */
  .letterhead{left:180px;top:19px;width:456px;height:624px;z-index:1}
  .letterhead .wordmark{padding-top:40px;font-size:19px}
  .letterhead .foot-band{position:absolute;left:0;right:0;bottom:20px;height:16px;background:var(--charcoal);border-top:2px solid var(--accent-red);color:#fff;font-size:6px;display:flex;align-items:center;justify-content:space-around;padding:0 12px}
  .letterhead .foot-web{position:absolute;left:0;right:0;bottom:8px;text-align:center;font-size:6px;color:var(--ink)}

  /* business card, laid over the letterhead edge */
  .card-front{left:29px;top:132px;width:192px;height:96px;background:var(--maroon);z-index:2}
  .card-front .wordmark{position:absolute;left:10px;top:14px;text-align:left;font-size:10.5px}
  .card-front .wordmark .name{letter-spacing:.2px}
  .card-front .wordmark .tag{letter-spacing:2.5px}
  .card-front .wordmark .mark-dot{width:9px;height:9px;margin:0 0 4px 0}
  .card-front .web{position:absolute;left:10px;right:10px;bottom:12px;padding-top:4px;border-top:1px solid rgba(255,255,255,.35);font-size:6px;color:var(--card-tint);letter-spacing:.3px}
  .card-back{left:29px;top:240px;width:192px;height:115px;z-index:2}
  .card-back .wordmark{padding-top:12px;font-size:9px}
  .card-back .wordmark .name{letter-spacing:.2px}
  .card-back .wordmark .mark-dot{width:8px;height:8px;margin-bottom:4px}
  .card-back .name-band{position:absolute;left:0;right:0;top:62px;height:13px;background:var(--charcoal);color:#fff;font-size:6px;padding:3px 8px;white-space:nowrap}
  .card-back .name-band b{font-weight:700}
  .card-back .contact{position:absolute;left:8px;top:82px;font-size:5px;line-height:8px;color:var(--ink);white-space:nowrap}

  /* envelopes */
  .envelope-back{left:653px;top:82px;width:523px;height:254px}
  .envelope-back .flap{display:block;position:absolute;left:0;top:0}
  .envelope-back .wordmark{position:absolute;left:0;right:0;top:16px;font-size:16px}
  .envelope-front{left:653px;top:360px;width:523px;height:218px}
  .envelope-front .wordmark{padding-top:40px;font-size:16px}
  .envelope-front .foot-line{position:absolute;left:0;right:0;bottom:37px;height:2px;background:var(--accent-red)}
  .envelope-front .foot-band{position:absolute;left:0;right:0;bottom:22px;height:14px;background:var(--charcoal);color:#fff;font-size:5.5px;display:flex;align-items:center;justify-content:space-around;padding:0 10px}
</style>
</head>
<body>
<main class="canvas">

  <section class="sheet letterhead">
    <div class="wordmark"><span class="mark-dot"></span><span class="name">Skyreach Northern Flights</span><span class="tag">Private Charters</span></div>
    <div class="foot-band">
      <span>5127 N. Darrow, Suite 240 Scottsdale, AZ 85254</span>
      <span>P 480.555.0142</span>
      <span>F 480.555.0143</span>
      <span>tholbrook@skyreachnorthernflights.example</span>
    </div>
    <div class="foot-web">www.skyreachnorthernflights.example</div>
  </section>

  <section class="sheet card-front">
    <div class="wordmark light"><span class="mark-dot"></span><span class="name">Skyreach Northern Flights</span><span class="tag">Private Charters</span></div>
    <div class="web">www.skyreachnorthernflights.example</div>
  </section>

  <section class="sheet card-back">
    <div class="wordmark"><span class="mark-dot"></span><span class="name">Skyreach Northern Flights</span><span class="tag">Private Charters</span></div>
    <div class="name-band"><b>Tamara Holbrook</b> | Business Development</div>
    <div class="contact">
      P 480.555.0142 &nbsp; F 480.555.0143<br>
      tholbrook@skyreachnorthernflights.example
    </div>
  </section>

  <section class="sheet envelope-back">
    <svg class="flap" width="523" height="100" viewBox="0 0 523 100" aria-hidden="true">
      <path d="M0 0 H523 V64 Q523 78 508 80 L275 98 Q261 100 248 98 L15 80 Q0 78 0 64 Z" fill="#5c5755"/>
      <path d="M0 64 Q0 78 15 80 L248 98 Q261 100 275 98 L508 80 Q523 78 523 64" fill="none" stroke="#8e2c25" stroke-width="2"/>
    </svg>
    <div class="wordmark light"><span class="mark-dot"></span><span class="name">Skyreach Northern Flights</span><span class="tag">Private Charters</span></div>
  </section>

  <section class="sheet envelope-front">
    <div class="wordmark"><span class="mark-dot"></span><span class="name">Skyreach Northern Flights</span><span class="tag">Private Charters</span></div>
    <div class="foot-line"></div>
    <div class="foot-band">
      <span>5127 N. Darrow, Suite 240 Scottsdale, AZ 85254</span>
      <span>P 480.555.0142</span>
      <span>F 480.555.0143</span>
      <span>www.skyreachnorthernflights.example</span>
    </div>
  </section>

</main>
</body>
</html>
```